Pellmark Ridgeway LLC stationery, business card and web page design.

i need a full set of stationery designed using the name "Pellmark Ridgeway LLC" with a tag line "construction consulting services". using the uploaded monkey icon as the logo.

i like the colors orange, green and black in general but im not limited to that. the company offers consulting services to various types of construction businesses.

i travel around the country in a 4x4 camper offering consulting services and technical training short term and long to various types of construction companies.

Construction Company

Peter Lund
p.lund@pellmarkridgeway.example
2748 Fenwick Rd
Maple Glen, NY 10943
555 014 3627

list these services on the card.

Business Consulting
Capital Investments
Marketing Implementations
Technical Training

1 page

Designer to choose colors to be used in the design.

• company info and use of the monkey icon i provided.
• a fun but professional design
• the color red

```html
<!DOCTYPE html>
<html lang="en">
<head>
<meta charset="utf-8">
<title>Pellmark Ridgeway LLC – Stationery</title>
<link rel="stylesheet" href="https://fonts.googleapis.com/css2?family=Titillium+Web:wght@400;600&family=Carlito:ital,wght@0,400;1,400&display=swap">
<style>
  :root {
    --orange: #f0642a;
    --black: #231f20;
    --paper: #ffffff;
    --ink: #4a4a4a;
    --navy: #1c1f4a;
    --stage: #3b3b3b;
    --watermark: #ececec;
  }
  * { margin: 0; padding: 0; box-sizing: border-box; }
  html, body { width: 1200px; height: 1200px; overflow: hidden; }
  body { background: var(--stage); position: relative; font-family: "Carlito", sans-serif; }

  .brand-name {
    font-family: "Titillium Web", sans-serif;
    font-weight: 600;
    color: var(--orange);
    line-height: 1;
  }
  .brand-mark { border-radius: 50%; background: var(--black); position: absolute; }

  /* Letterhead */
  .letterhead {
    position: absolute; left: 143px; top: 126px; width: 772px; height: 997px;
    background: var(--paper); overflow: hidden;
  }
  .letterhead .brand-mark { left: 28px; top: 28px; width: 92px; height: 92px; }
  .letterhead .brand-name { position: absolute; left: 135px; top: 42px; font-size: 34px; line-height: 38px; }
  .letterhead .watermark {
    position: absolute; left: 490px; top: 790px; width: 270px; height: 270px;
    border-radius: 50%; background: var(--watermark);
  }
  .recipient { position: absolute; left: 57px; top: 183px; font-size: 13.5px; line-height: 25.6px; color: var(--ink); }
  .letter-body { position: absolute; left: 57px; top: 283px; width: 690px; font-size: 13.5px; line-height: 25.6px; color: var(--ink); }
  .letter-body p { margin-bottom: 25.6px; white-space: nowrap; }
  .closing { position: absolute; left: 62px; top: 797px; font-family: "Titillium Web", sans-serif; font-size: 22px; color: var(--ink); }
  .signature { position: absolute; left: 61px; top: 832px; font-style: italic; font-size: 30px; color: var(--navy); }
  .letterhead .tagline {
    position: absolute; left: 25px; top: 930px; font-family: "Titillium Web", sans-serif;
    font-size: 21px; color: var(--black);
  }
  .footer-bar { position: absolute; }
  .footer-bar.main { left: 0; top: 964px; width: 509px; height: 14px; background: var(--orange); }
  .footer-bar.thin { left: 515px; top: 967px; width: 133px; height: 5px; background: var(--orange); }
  .footer-bar.dark { left: 658px; top: 964px; width: 114px; height: 14px; background: var(--black); }

  /* Business cards */
  .card { position: absolute; background: var(--orange); overflow: hidden; }
  .card-front { left: 526px; top: 175px; width: 306px; height: 175px; }
  .card-front .brand-name {
    position: absolute; left: 22px; top: 30px; color: var(--paper);
    font-size: 34px; line-height: 34px; text-transform: uppercase;
  }
  .card-front .tagline {
    position: absolute; left: 24px; top: 104px; font-family: "Titillium Web", sans-serif;
    font-size: 12px; color: var(--black);
  }
  .card-front .brand-mark { right: 16px; bottom: -20px; width: 70px; height: 70px; }
  .card-back { left: 530px; top: 386px; width: 299px; height: 170px; display: flex; align-items: center; justify-content: center; }
  .card-back .brand-name { color: var(--black); font-size: 22px; }

  /* Envelope */
  .envelope { position: absolute; left: 338px; top: 625px; width: 808px; height: 351px; background: var(--paper); }
  .envelope .band-accent { position: absolute; top: 118px; height: 115px; background: var(--orange); }
  .envelope .band-accent.left { left: 0; width: 35px; }
  .envelope .band-accent.right { left: 361px; width: 43px; }
  .envelope .band-dark {
    position: absolute; left: 404px; top: 118px; width: 404px; height: 115px; background: var(--black);
    display: flex; align-items: center; padding-left: 27px;
    font-family: "Titillium Web", sans-serif; font-size: 26px; color: var(--paper);
  }
  .envelope .brand-mark { left: 52px; top: 128px; width: 92px; height: 92px; }
  .envelope .brand-name { position: absolute; left: 155px; top: 137px; font-size: 32px; line-height: 36px; }
</style>
</head>
<body>
  <section class="letterhead">
    <div class="watermark"></div>
    <div class="brand-mark"></div>
    <div class="brand-name">Pellmark<br>Ridgeway LLC</div>

    <div class="recipient">To<br>The,<br>Director</div>

    <div class="letter-body">
      <p>Lorem ipsum dolor sit amet, consectetur adipiscing elit. Integer nec odio. Praesent libero. Sed cursus ante<br>
      dictum, massa quam dapibus leo, eget vulputate orci purus ut lorem. In fermentum posuere urna nec scelerisque<br>
      aliquam quam vel dolor. Nunc adipiscing. Sed quamodo lacus in velit luctus sodales. Proin quam nibh etiam.<br>
      Vestibulum ut nulla aliquam risus rutrum interdum. Pellentesque lorem. Curabitur sit amet erat quis risus.</p>
      <p>Curabitur sit amet &nbsp;erat quis risus feugiat viverra. Pellentesque augue justo, sagittis et, lacinia at, venenatis<br>
      non, arcu. &nbsp;Nunc nec libero. In cursus dictum risus. Etiam tristique nisl a nulla. Ut a orci. Curabitur<br>
      dolonunc,egestas at, accumsan at, malesuada nec, magna. Nulla facilisi. Nunc volutpat. &nbsp;Vestibulum ante<br>
      ipsum primis in faucibus orci luctus et ultrices posuere cubilia Curae. Ut sit amet orci vel mauris blandit<br>
      vehicula. Nullam quis enim. Integer dignissim viverra velit. Curabitur in odio.</p>
      <p>In hac habitasse platea dictumst. Ut quis nisl. Nunc nunc quam, tempus sit amet, sollicitudin nec.<br>
      imperdiet nulla tellus ut diam. Vestibulum ipsum ante, malesuada quis, tempus ac, placerat sit amet.</p>
      <p>Curabitur sit amet &nbsp;erat quis risus feugiat viverra. Pellentesque augue justo, sagittis et, lacinia at.<br>
      non, arcu. &nbsp;Nunc nec libero. In cursus dictum risus. Etiam tristique nisl a nulla. Ut a orci.<br>
      dolonunc,egestas at, accumsan at, malesuada nec, magna. Nulla facilisi. Nunc volutpat.<br>
      ipsum primis in faucibus orci luctus et ultrices posuere cubilia Curae.<br>
      vehicula. Nullam quis enim. Integer dignissim viverra velit.</p>
    </div>

    <div class="closing">Thanking you,</div>
    <div class="signature">Alex Marsh</div>

    <div class="tagline">construction consulting services</div>
    <div class="footer-bar main"></div>
    <div class="footer-bar thin"></div>
    <div class="footer-bar dark"></div>
  </section>

  <section class="card card-front">
    <div class="brand-name">Pellmark<br>Ridgeway LLC</div>
    <div class="tagline">construction consulting services</div>
    <div class="brand-mark"></div>
  </section>

  <section class="card card-back">
    <div class="brand-name">Pellmark Ridgeway LLC</div>
  </section>

  <section class="envelope">
    <div class="band-accent left"></div>
    <div class="brand-mark"></div>
    <div class="brand-name">Pellmark<br>Ridgeway LLC</div>
    <div class="band-accent right"></div>
    <div class="band-dark">construction consulting services</div>
  </section>
</body>
</html>
```